Dr Mira Thalen, Orthopaedic Hand Surgeon

I am an orthopaedic hand surgeon and need business cards that reflect the surgery I do. I operate on bones, ligaments, tendons, and soft tissues. I can do microsurgery (surgery under an operating microscope) - including connecting ends of cut nerves and arteries in the fingers together. As an orthopaedic surgeon, I also fix fractures and manage orthopaedic trauma in the rest of the body. I favour black as a colour, and have some pictures of hand X-rays that you can use in the design, if you think that would look good (feel free to crop).
Updates

Hi all. Thank you for all your submissions so far. Please note that I have updated my project brief. I would like to emphasise that use of the logos that I have provided is optional, and if used, I would very much prefer the logo not to dominate the card, but add to the overall aesthetic of the card. Warm regards, Mira

Target Market(s)

Referring medical practitioners, hand therapists, patients

Industry/Entity Type

Healthcare

Contact Information for Business Card

Dr Mira Thalen
Orthopaedic Hand Surgeon
MBBS BSc (Med), MIntPH (Merit), FCWES (Ortho), FUPelV

Font styles to use
Serif

Colors

Designer to choose colors to be used in the design.

Requirements
Must have
• Space for:
• 2 addresses (a PO Box Address and a consulting suite address) - to be confirmed
• 1 phone number - to be confirmed
Nice to have
• Please choose one of the FCWES logos (I included 3 - colour, black reverse, and greyscale); if you include this in the design, IT SHOULD NOT DOMINATE THE CARD, but be smaller and more discreet.
• I have also attached the FUPelV logo (colour and greyscale); if you choose to include this in the design, IT SHOULD NOT DOMINATE THE CARD, but be smaller and more discreet.
• I would love to be able to update details on the card as time goes on, and thus would like to own the template for the card as well.
• Also I would love discussion with regard to any changes on the card, if I am not completely happy with the design, and would like to discuss things such as ease of printing, finish on the cards (matte, polish) etc.
Should not have
• I don't like the card to look too crowded

```html
<!DOCTYPE html>
<html lang="en">
<head>
<meta charset="utf-8">
<title>Dr Mira Thalen – Business Card</title>
<link href="https://fonts.googleapis.com/css2?family=Montserrat:wght@400;500;600;700&display=swap" rel="stylesheet">
<style>
  :root{
    --bg:#2b2d31;
    --card-black:#1f1f21;
    --card-back:#151516;
    --paper:#f1f1ef;
    --blue:#1d5d80;
    --blue-light:#3d86ad;
    --blue-line:#4a9cc9;
    --ink-white:#ffffff;
    --ink-soft:#c9cbcf;
    --logo-grey:#a8a9ac;
  }
  *{margin:0;padding:0;box-sizing:border-box}
  html,body{width:1200px;height:1000px;overflow:hidden}
  body{background:var(--bg);font-family:"Montserrat",Arial,sans-serif;position:relative}

  .card{position:absolute;border-radius:22px;overflow:hidden;box-shadow:0 14px 30px rgba(0,0,0,.45)}

  /* Front card */
  .card-front{left:110px;top:190px;width:360px;height:620px;background:var(--card-black)}
  .front-curve{position:absolute;left:0;top:0}
  .college-mark{position:absolute;left:40px;top:70px;color:var(--blue)}
  .college-mark__row{display:flex;align-items:center;gap:10px}
  .college-mark__square{width:22px;height:22px;background:var(--blue)}
  .college-mark__name{font-size:34px;font-weight:500;letter-spacing:1px;line-height:1}
  .college-mark__caption{margin-top:8px;font-size:9px;font-weight:500;color:var(--blue);line-height:1.4;text-align:right;width:200px}

  .details{position:absolute;left:40px;top:340px;width:280px;color:var(--ink-white)}
  .details__name{font-size:19px;font-weight:700}
  .details__role{font-size:15px;font-weight:600;margin-top:3px}
  .details__creds{font-size:10px;color:var(--ink-soft);margin-top:6px;line-height:1.45}
  .rule{height:1px;background:var(--blue-line);margin:12px 0}
  .address{font-size:14px;line-height:1.35}
  .contact{list-style:none;font-size:14px;line-height:1.6}
  .contact li{display:flex;align-items:center;gap:10px}
  .contact svg{flex:none}
  .contact .web{font-weight:700}

  /* Back card */
  .card-back{left:520px;top:320px;width:640px;height:370px;background:linear-gradient(160deg,#2a2a2c,var(--card-back) 70%)}
  .back-mark{position:absolute;left:50px;top:50px;color:var(--logo-grey)}
  .back-mark .college-mark__square{background:var(--logo-grey)}
  .back-mark .college-mark__caption{color:var(--logo-grey);width:240px;font-size:11px}
  .back-mark .college-mark__name{font-size:40px}
  .xray{position:absolute;right:0;top:40px;width:330px;height:330px;
        background:radial-gradient(ellipse at 55% 45%,#d7d8da 0%,#8b8d90 30%,#3b3c3e 60%,rgba(21,21,22,0) 80%);opacity:.85}
</style>
</head>
<body>

  <section class="card card-front">
    <svg class="front-curve" width="360" height="620" viewBox="0 0 360 620" aria-hidden="true">
      <defs>
        <linearGradient id="bandGrad" x1="0" y1="0" x2="1" y2="1">
          <stop offset="0" stop-color="#dfe6ea"/>
          <stop offset=".5" stop-color="#3d86ad"/>
          <stop offset="1" stop-color="#174c6a"/>
        </linearGradient>
      </defs>
      <path d="M0 0 H360 V150 C360 250 250 320 0 312 Z" fill="url(#bandGrad)"/>
      <path d="M0 0 H300 C345 80 345 170 310 220 C260 285 140 300 0 290 Z" fill="#f1f1ef"/>
    </svg>

    <div class="college-mark">
      <div class="college-mark__row">
        <span class="college-mark__square"></span>
        <span class="college-mark__name">FCWES</span>
      </div>
      <p class="college-mark__caption">Fellow of the<br>Collegium of Western Surgeons</p>
    </div>

    <div class="details">
      <h1 class="details__name">Dr Mira Thalen</h1>
      <p class="details__role">Orthopaedic Hand Surgeon</p>
      <p class="details__creds">MBBS BSc (Med), MIntPH (Merit),<br>FCWES (Ortho), FUPelV</p>
      <div class="rule"></div>
      <p class="address">42 Harlow Lane<br>Dunmore, AK 90418</p>
      <div class="rule"></div>
      <p class="address">250 Orchard Row Ste 12<br>Linden, UT 81204-5530</p>
      <div class="rule"></div>
      <ul class="contact">
        <li><svg width="14" height="14" viewBox="0 0 14 14"><circle cx="7" cy="7" r="7" fill="#fff"/><path d="M4.5 3.5l1.5 1.5-.8 1c.5 1 1.3 1.8 2.3 2.3l1-.8 1.5 1.5-1 1.2C6.5 10 4 7.5 3.3 4.5z" fill="#1f1f21"/></svg>900-555-0142</li>
        <li><svg width="14" height="14" viewBox="0 0 14 14"><rect x="1" y="3" width="12" height="8" fill="none" stroke="#fff" stroke-width="1.3"/><path d="M1 3l6 5 6-5" fill="none" stroke="#fff" stroke-width="1.3"/></svg>fcwes@surgeonsmail.com</li>
        <li class="web"><svg width="14" height="14" viewBox="0 0 14 14"><circle cx="7" cy="7" r="6" fill="none" stroke="#fff" stroke-width="1.3"/><ellipse cx="7" cy="7" rx="2.5" ry="6" fill="none" stroke="#fff" stroke-width="1"/><path d="M1 7h12" stroke="#fff" stroke-width="1"/></svg>www.fcwes-cards.com</li>
      </ul>
    </div>
  </section>

  <section class="card card-back">
    <div class="college-mark back-mark">
      <div class="college-mark__row">
        <span class="college-mark__square"></span>
        <span class="college-mark__name">FCWES</span>
      </div>
      <p class="college-mark__caption">Fellow of the<br>Collegium of Western Surgeons</p>
    </div>
    <div class="xray" role="img" aria-label="X-ray image of a hand and wrist"></div>
  </section>

</body>
</html>
```